Pristwell Recovery Email Marketing Design

Dear Designer,
We're in need of an email background template for our company, Pristwell Recovery, that reflects our commitment to building lasting relationships with our clients and providing top-quality restoration and cleaning services.
We'd like the template to incorporate our brand colors, which are #F2F2F3, #005EA5, #468ECC, and #000000, and to feature images related to our services, such as water restoration, emergency flood response, mold remediation, trauma scene clean-up, fire restoration, carpet cleaning, and more. Our logo and tagline, "Disaster Undone", should be prominently displayed in a unique and visually appealing way, along with our website address, www.pristwellrecovery.example.
The email should be professional and positive, highlighting the camaraderie and teamwork among our employees. We want to thank our clients for their business, offer a special discount, and promote our services. The final design should be visually stunning and memorable, with a clear call-to-action to encourage clients to take advantage of the discount.
We'd like the final design in JPG or PNG format, with a resolution of at least 720x720 pixels.
Thank you for considering this project. We're excited to see what you come up with!
Best regards,
Dabney
Look and feel
Each slider illustrates characteristics of the customer's brand and the style your logo design should communicate.

```html
<!DOCTYPE html>
<html lang="en">
<head>
<meta charset="utf-8">
<title>Pristwell Recovery – Disaster Undone</title>
<link rel="stylesheet" href="https://fonts.googleapis.com/css2?family=Poppins:wght@600;700;800&family=Arimo:wght@400;700&display=swap">
<style>
  :root {
    --light: #F2F2F3;
    --blue-deep: #005EA5;
    --blue-sky: #468ECC;
    --black: #000000;
    --ink-soft: #1b1b1d;
    --white: #ffffff;
    --grey-client: #9a9a9e;
    --hero-light: #e6e3dd;
    --hero-mid: #c9c6c1;
    --hero-dark: #4a4e5e;
  }
  * { box-sizing: border-box; margin: 0; padding: 0; }
  html, body { width: 1200px; height: 1200px; overflow: hidden; background: var(--black); }
  .email {
    position: relative; width: 1200px; height: 1200px; overflow: hidden;
    background: radial-gradient(ellipse at 50% 35%, #26272b 0%, #0d0d0f 60%, var(--black) 100%);
    font-family: "Arimo", Arial, sans-serif; color: var(--white);
  }
  .brand-plate {
    position: absolute; left: 430px; top: 0; width: 340px; height: 125px;
    background: linear-gradient(180deg, #2c2f36 0%, #14161a 100%);
    display: flex; align-items: center; justify-content: center;
  }
  .brand-name {
    font-family: "Poppins", sans-serif; font-weight: 700; font-size: 30px;
    color: var(--light); letter-spacing: 1px; text-transform: uppercase;
  }
  .hero {
    position: absolute; left: 0; top: 128px; width: 1200px; height: 385px;
    background: linear-gradient(90deg, var(--hero-light) 0%, var(--hero-light) 38%, var(--hero-mid) 55%, var(--hero-dark) 75%, var(--hero-mid) 92%, var(--hero-light) 100%);
  }
  .offer-bubble { position: absolute; left: 345px; top: 133px; width: 140px; height: 80px; }
  .offer-text {
    position: absolute; left: 345px; top: 144px; width: 134px; text-align: center;
    font-family: "Poppins", sans-serif; font-weight: 700; font-size: 19px; line-height: 22px;
    color: var(--blue-deep);
  }
  .tagline {
    position: absolute; left: 60px; top: 220px;
    font-family: "Poppins", sans-serif; font-weight: 800; font-size: 72px; line-height: 90px;
    letter-spacing: 1px;
    background: linear-gradient(180deg, var(--blue-sky) 0%, var(--blue-deep) 100%);
    -webkit-background-clip: text; background-clip: text; color: transparent;
  }
  .book-now {
    position: absolute; left: 48px; top: 416px; width: 184px; height: 60px;
    border: 3px solid var(--blue-deep); border-radius: 30px;
    display: flex; align-items: center; justify-content: center;
    font-family: "Poppins", sans-serif; font-weight: 700; font-size: 21px; color: var(--blue-deep);
  }
  .section-title {
    position: absolute; left: 0; width: 1200px; text-align: center;
    font-family: "Poppins", sans-serif; font-weight: 700; font-size: 35px; color: var(--blue-sky);
  }
  .services-title { top: 550px; }
  .clients-title { top: 815px; }
  .service { position: absolute; top: 622px; width: 260px; text-align: center; }
  .service-icon {
    width: 96px; height: 96px; margin: 0 auto 18px; border-radius: 14px;
    background: var(--ink-soft);
  }
  .service-label { font-weight: 700; font-size: 22px; line-height: 28px; color: var(--white); }
  .client {
    position: absolute; top: 900px; width: 220px; text-align: center;
    font-weight: 700; font-size: 28px; color: var(--grey-client);
  }
  .contact-band {
    position: absolute; left: 0; top: 1003px; width: 1200px; height: 119px; background: var(--blue-deep);
  }
  .contact-item { position: absolute; top: 0; height: 119px; display: flex; align-items: center; }
  .contact-badge {
    width: 74px; height: 74px; border-radius: 50%; background: var(--white);
    display: flex; align-items: center; justify-content: center; flex: none;
  }
  .contact-text { margin-left: 18px; font-size: 19px; line-height: 28px; color: var(--white); }
  .footer {
    position: absolute; left: 0; top: 1122px; width: 1200px; height: 78px;
    display: flex; align-items: center; font-size: 19px; color: var(--white);
  }
  .copyright { position: absolute; left: 100px; }
  .site { position: absolute; left: 775px; display: flex; align-items: center; color: var(--blue-sky); }
  .site svg { margin-right: 8px; }
</style>
</head>
<body>
<main class="email">
  <div class="brand-plate"><span class="brand-name">Pristwell Recovery</span></div>

  <section class="hero" role="img" aria-label="Photo of a technician in a cap and work uniform kneeling to lift a carpet edge"></section>

  <svg class="offer-bubble" viewBox="0 0 140 80" aria-hidden="true">
    <path d="M70 4 C108 4 136 18 136 36 C136 55 108 68 70 68 C60 68 50 67 42 65 L22 77 L28 60 C12 54 4 46 4 36 C4 18 32 4 70 4 Z" fill="none" stroke="#005EA5" stroke-width="3"/>
  </svg>
  <div class="offer-text">50%<br>OFFER</div>

  <h1 class="tagline">DISASTER<br>UNDONE</h1>
  <div class="book-now">BOOK NOW</div>

  <h2 class="section-title services-title">OUR SERVICES</h2>
  <div class="service" style="left:58px">
    <div class="service-icon" role="img" aria-label="Line icon of a dripping faucet with water drops"></div>
    <div class="service-label">Water Restoration</div>
  </div>
  <div class="service" style="left:342px">
    <div class="service-icon" role="img" aria-label="Line icon of a leaking pipe over a basin"></div>
    <div class="service-label">Mold Remediation</div>
  </div>
  <div class="service" style="left:627px">
    <div class="service-icon" role="img" aria-label="Line icon of a fire extinguisher and flame"></div>
    <div class="service-label">Fire and Smoke<br>Restoration</div>
  </div>
  <div class="service" style="left:890px">
    <div class="service-icon" role="img" aria-label="Line icon of an injured person with a bandage"></div>
    <div class="service-label">Trauma Clean Up</div>
  </div>

  <h2 class="section-title clients-title">OUR CLIENTS</h2>
  <div class="client" style="left:260px">Tidecrest</div>
  <div class="client" style="left:453px">Brookline</div>
  <div class="client" style="left:687px">Verano</div>

  <section class="contact-band">
    <div class="contact-item" style="left:101px">
      <div class="contact-badge">
        <svg width="26" height="34" viewBox="0 0 24 32" aria-hidden="true"><path d="M12 0C5.4 0 0 5.3 0 11.8 0 20.6 12 32 12 32s12-11.4 12-20.2C24 5.3 18.6 0 12 0zm0 16.5a4.7 4.7 0 1 1 0-9.4 4.7 4.7 0 0 1 0 9.4z" fill="#005EA5"/></svg>
      </div>
      <div class="contact-text">4810 Alder Ridge Rd #12<br>Harborview, NV 89000</div>
    </div>
    <div class="contact-item" style="left:443px">
      <div class="contact-badge">
        <svg width="30" height="30" viewBox="0 0 24 24" aria-hidden="true"><path d="M6.6 10.8c1.4 2.8 3.8 5.1 6.6 6.6l2.2-2.2c.3-.3.7-.4 1-.2 1.1.4 2.3.6 3.6.6.6 0 1 .4 1 1V20c0 .6-.4 1-1 1C10.6 21 3 13.4 3 4c0-.6.4-1 1-1h3.5c.6 0 1 .4 1 1 0 1.3.2 2.5.6 3.6.1.3 0 .7-.2 1l-2.3 2.2z" fill="#005EA5"/></svg>
      </div>
      <div class="contact-text">(555) 014-2736</div>
    </div>
    <div class="contact-item" style="left:703px">
      <div class="contact-badge">
        <svg width="30" height="24" viewBox="0 0 30 22" aria-hidden="true"><rect x="0" y="0" width="30" height="22" rx="3" fill="#005EA5"/><path d="M1 2 L15 12 L29 2" fill="none" stroke="#ffffff" stroke-width="2.4"/></svg>
      </div>
      <div class="contact-text">support@pristwellrecovery.example</div>
    </div>
  </section>

  <footer class="footer">
    <span class="copyright">©Copyrights 2023 Pristwell Recovery &nbsp;&nbsp;|&nbsp;&nbsp; All Rights Reserved</span>
    <span class="site">
      <svg width="20" height="20" viewBox="0 0 20 20" aria-hidden="true"><circle cx="10" cy="10" r="9" fill="none" stroke="#468ECC" stroke-width="1.8"/><ellipse cx="10" cy="10" rx="4" ry="9" fill="none" stroke="#468ECC" stroke-width="1.6"/><line x1="1" y1="10" x2="19" y2="10" stroke="#468ECC" stroke-width="1.6"/></svg>
      www.pristwellrecovery.example
    </span>
  </footer>
</main>
</body>
</html>
```